Design Business Cards

Contest for a design for our new business cards. We are an energy company that provides energy services to businesses. Please visit our website [url removed, login to view] for more information. The cards should be 2 sided so the back cannot be written on (dark color). They should also prominently display the attached logo. The exact template that will be needed for the printer (Kelto Press) is attached, please make sure your design complies to these specifications.

Thanks and good luck!

```html
<!DOCTYPE html>
<html lang="en">
<head>
<meta charset="utf-8">
<title>Halden Power Business Cards</title>
<link rel="stylesheet" href="https://fonts.googleapis.com/css2?family=Arimo:wght@400;700&display=swap">
<style>
  :root {
    --page-bg: #d9d9d9;
    --card-dark: #141112;
    --card-light: #ffffff;
    --ink: #222222;
    --gold: #c98a2e;
    --green: #3aa648;
    --orange: #e8892b;
    --red: #c4242b;
    --url-green: #27b24a;
  }
  * { margin: 0; padding: 0; box-sizing: border-box; }
  html, body { width: 1200px; height: 680px; overflow: hidden; }
  body {
    background: var(--page-bg);
    font-family: "Arimo", Arial, sans-serif;
    position: relative;
  }
  .card {
    position: absolute;
    top: 190px;
    width: 520px;
    height: 298px;
    overflow: hidden;
    box-shadow: 0 6px 18px rgba(0,0,0,0.25);
  }
  /* Front */
  .card-front { left: 50px; display: flex; background: var(--card-light); }
  .front-side {
    width: 150px;
    background: var(--card-dark);
    border-right: 4px solid var(--gold);
    display: flex;
    flex-direction: column;
    align-items: center;
    justify-content: center;
    gap: 40px;
  }
  .side-brand {
    color: var(--orange);
    font-weight: 700;
    font-size: 17px;
    text-align: center;
    line-height: 1.2;
  }
  .side-url { color: var(--url-green); font-size: 12px; }
  .front-main { flex: 1; padding: 38px 30px 0 26px; color: var(--ink); }
  .brand {
    display: flex;
    align-items: center;
    gap: 8px;
    color: var(--orange);
    font-weight: 700;
    font-size: 22px;
  }
  .brand-square { width: 14px; height: 14px; background: var(--orange); }
  .person { margin-top: 14px; font-size: 17px; }
  .person-name { font-weight: 700; }
  .person-role { font-size: 14px; }
  .contacts { list-style: none; margin-top: 18px; font-size: 13px; line-height: 1.6; }
  .contacts li { display: flex; gap: 8px; align-items: flex-start; }
  .tag {
    display: inline-block;
    width: 16px; height: 16px;
    margin-top: 2px;
    color: #fff;
    font-size: 10px;
    font-weight: 700;
    text-align: center;
    line-height: 16px;
    flex-shrink: 0;
  }
  .tag-phone { background: var(--green); }
  .tag-email { background: var(--orange); }
  .tag-address { background: var(--red); }
  /* Back */
  .card-back { left: 630px; background: var(--card-dark); }
  .back-frame {
    position: absolute;
    inset: 18px;
    border: 3px solid var(--gold);
  }
  .back-content {
    position: absolute;
    inset: 0;
    display: flex;
    flex-direction: column;
    align-items: center;
    justify-content: center;
    text-align: center;
  }
  .back-brand {
    color: var(--orange);
    font-weight: 700;
    font-size: 26px;
    margin-bottom: 26px;
  }
  .back-call { color: var(--red); font-size: 15px; }
  .back-url { color: var(--url-green); font-size: 15px; margin-top: 4px; }
</style>
</head>
<body>
  <section class="card card-front">
    <div class="front-side">
      <div class="side-brand">Halden<br>Power</div>
      <div class="side-url">www.HaldenPower.com</div>
    </div>
    <div class="front-main">
      <div class="brand"><span class="brand-square"></span>Halden Power</div>
      <p class="person"><span class="person-name">Mara Ellis</span> <span class="person-role">|Managing Director</span></p>
      <ul class="contacts">
        <li><span class="tag tag-phone">t.</span>1-800-555-0142</li>
        <li><span class="tag tag-email">e.</span>info@haldenpower.com</li>
        <li><span class="tag tag-address">a.</span><span>410 Harbor Point Road, 6th Floor<br>Lakeview Bay FL 30210</span></li>
      </ul>
    </div>
  </section>

  <section class="card card-back">
    <div class="back-frame"></div>
    <div class="back-content">
      <div class="back-brand">Halden Power</div>
      <div class="back-call">Call Today 1-800-555-0142</div>
      <div class="back-url">www.HaldenPower.com</div>
    </div>
  </section>
</body>
</html>
```